Business card for home decor store and design

I need a business card for my home decor boutique that’s professional looking boho/rustic. We sell vintage furniture, vintage finds, lamps, throws, rugs. We also carry a Diy paint line for refinishing furniture. We offer workshop on painting furniture, private or group setting. We in the heart of Old Town Red Bluff. We love to design, build and restore. Family owned small business. Our style is rustic boho farmhouse. We search for one of a kind found and repurposed items. We love vintage home decor, vintage windows.

Target Market(s)

Home decor

Industry/Entity Type

Home Accessories

Contact Information for Business Card

Have a rustic look/boho

Font styles to use
Serif
Script

Requirements
Must have
• Logo

```html
<!DOCTYPE html>
<html lang="en">
<head>
<meta charset="utf-8">
<title>Birch &amp; Loom Co. — Business Card</title>
<link rel="stylesheet" href="https://fonts.googleapis.com/css2?family=Lora:wght@400;700&display=swap">
<style>
  :root {
    --page-bg: #e9e6e2;
    --card-top-a: #f4f3f1;
    --card-top-b: #dfe4ea;
    --band: #141414;
    --band-edge: #2a2a2a;
    --ink: #1b1b1b;
    --ink-soft: #2e2e2e;
    --contact: #cbbab2;
    --address: #9a8479;
    --seal: #dcd8d6;
    --icon: #bdb2ad;
  }
  * { box-sizing: border-box; margin: 0; padding: 0; }
  html, body { width: 1200px; height: 970px; overflow: hidden; }
  body {
    background: var(--page-bg);
    font-family: "Lora", Georgia, serif;
    position: relative;
  }
  .card {
    position: absolute;
    left: 70px; top: 183px;
    width: 1060px; height: 604px;
    overflow: hidden;
    background: linear-gradient(100deg, var(--card-top-a) 0%, var(--card-top-b) 55%, var(--card-top-a) 100%);
    box-shadow: 0 18px 40px rgba(0,0,0,0.18);
  }
  .card__band {
    position: absolute;
    left: 0; right: 0; top: 324px; bottom: 0;
    background: linear-gradient(180deg, var(--band-edge) 0%, var(--band) 30%, var(--band) 100%);
  }
  .holder {
    position: absolute;
    left: 57px; top: 72px;
    color: var(--ink);
  }
  .holder__name {
    font-weight: 700;
    font-size: 31px;
    letter-spacing: 0.5px;
    line-height: 1.1;
  }
  .holder__role {
    font-size: 24px;
    color: var(--ink-soft);
    margin-top: 4px;
  }
  .brand {
    position: absolute;
    left: 361px; top: 169px;
    width: 336px; height: 336px;
    border-radius: 50%;
    background: var(--seal);
    display: flex; align-items: center; justify-content: center;
  }
  .brand__name {
    font-size: 34px;
    font-weight: 400;
    color: var(--ink);
    white-space: nowrap;
  }
  .contact {
    position: absolute;
    left: 57px; top: 454px;
    list-style: none;
    color: var(--contact);
    font-size: 25px;
  }
  .contact__item {
    display: flex; align-items: center;
    height: 35px;
  }
  .contact__icon {
    width: 22px; height: 22px;
    margin-right: 17px;
    fill: none; stroke: var(--icon); stroke-width: 1.6;
  }
  .address {
    position: absolute;
    left: 697px; top: 488px;
    color: var(--address);
    font-size: 25px;
    font-style: normal;
    line-height: 32px;
  }
</style>
</head>
<body>
  <article class="card">
    <div class="card__band"></div>

    <header class="holder">
      <h1 class="holder__name">MARA ELLISON</h1>
      <p class="holder__role">Director</p>
    </header>

    <div class="brand">
      <span class="brand__name">Birch &amp; Loom Co.</span>
    </div>

    <ul class="contact">
      <li class="contact__item">
        <svg class="contact__icon" viewBox="0 0 24 24" aria-hidden="true"><path d="M6 3l3 4-2 2c1 3 3 5 6 6l2-2 4 3-2 3C10 19 5 14 3 5z"/></svg>
        +1 555 014 2290
      </li>
      <li class="contact__item">
        <svg class="contact__icon" viewBox="0 0 24 24" aria-hidden="true"><rect x="3" y="6" width="18" height="12"/><path d="M3 6l9 7 9-7"/></svg>
        hello@birchandloom.com
      </li>
      <li class="contact__item">
        <svg class="contact__icon" viewBox="0 0 24 24" aria-hidden="true"><circle cx="12" cy="12" r="9"/><ellipse cx="12" cy="12" rx="4" ry="9"/><path d="M3 12h18M5 7h14M5 17h14"/></svg>
        www.birchandloom.com
      </li>
    </ul>

    <address class="address">
      PO BOX 48, Hawthorn Lane<br>
      2nd Street, Ashford
    </address>
  </article>
</body>
</html>
```